Quvanta Redesign

We need a face lift for our website, www.quvanta.com. We sell flooring and related products nationwide. We are interested in expanding the width of the website and introducing grays and black. We want the design to be both contemporary and user friendly.

```html
<!DOCTYPE html>
<html lang="en">
<head>
<meta charset="utf-8">
<title>Quvanta – Flooring</title>
<link href="https://fonts.googleapis.com/css2?family=Arimo:wght@400;700&display=swap" rel="stylesheet">
<style>
:root{
  --red:#c0131b;
  --blue:#1fb3e0;
  --orange:#f7a417;
  --ink:#333;
  --light:#f2f2f2;
  --panel:#dedede;
  --stage:#7a7a7a;
  --footer:#2b2b2b;
  --base:#111;
  --white:#fff;
}
*{margin:0;padding:0;box-sizing:border-box}
html,body{width:1200px;height:1000px;overflow:hidden;background:var(--white);font-family:"Arimo",Arial,sans-serif;color:var(--ink)}
.page{position:relative;width:1200px;height:1000px}
.abs{position:absolute}

/* header */
.brand{left:292px;top:30px;display:flex;align-items:center;gap:6px}
.brand-mark{width:18px;height:18px;background:var(--red)}
.brand-name{font-size:22px;font-weight:700;color:var(--ink)}
.tagline{left:316px;top:56px;font-size:6px;font-weight:700;color:var(--ink)}
.util{top:10px;font-size:7px;color:#999}
.util b{color:var(--orange);font-weight:400}
.proceed{left:875px;top:4px;width:70px;height:20px;background:#ececec;font-size:7px;color:#888;display:flex;align-items:center;justify-content:center}
.proceed-go{left:948px;top:4px;width:20px;height:20px;background:var(--blue)}
.nav{top:50px;font-size:7px;font-weight:700;color:#555}

.band{left:0;top:100px;width:1200px;height:543px;background:var(--light)}

/* sidebar */
.search{left:292px;top:86px;width:153px;height:28px;background:var(--red);padding:5px}
.search-field{width:122px;height:18px;background:var(--white);font-size:6px;color:#999;padding:6px 6px}
.search-btn{left:419px;top:91px;width:22px;height:18px;background:#222}
.side-head{left:292px;width:153px;height:22px;background:var(--red);border-radius:5px 5px 0 0;color:var(--white);font-size:8px;font-weight:700;padding:7px 12px}
.side-list{left:292px;width:153px;background:var(--white);padding:10px 14px 0;font-size:6.5px;color:#666;list-style:none}
.side-list li{height:13.6px}
.offer{left:292px;top:487px;width:153px;height:144px;background:var(--white);border:1px solid #ddd;padding:18px 15px}
.offer h3{font-size:10px;font-weight:400;color:var(--red);padding-bottom:8px;border-bottom:1px solid #e5e5e5}
.offer p{font-size:6.5px;line-height:14px;color:#888;margin-top:10px}
.offer p span{color:var(--blue)}
.promo-btn{left:308px;top:587px;width:98px;height:23px;background:var(--orange);font-size:6.5px;font-weight:700;color:#222;display:flex;align-items:center;justify-content:center}

/* hero */
.hero-frame{left:455px;top:86px;width:359px;height:214px;background:var(--white);border:1px solid #ddd}
.hero-art{left:463px;top:94px;width:344px;height:198px;background:radial-gradient(circle at 30% 40%,#e0242c,#a9070d)}
.samples{left:818px;top:104px;width:150px;height:196px;background:var(--white)}
.samples-title{left:818px;top:128px;width:150px;text-align:center;font-size:36px;font-weight:700;line-height:36px;color:var(--red)}
.samples-sub{left:818px;top:164px;width:150px;text-align:center;font-size:21px;color:#888;letter-spacing:.5px}
.samples-box{left:826px;top:202px;width:135px;height:89px;background:var(--red);color:var(--white);font-size:11px;line-height:14px;text-align:center;padding-top:31px}
.samples-notch{left:884px;top:196px;width:0;height:0;border-left:6px solid transparent;border-right:6px solid transparent;border-bottom:6px solid var(--red)}

/* special offer */
.special{left:455px;top:303px;width:513px;height:97px;background:var(--panel)}
.special-title{left:491px;top:325px;font-size:15px;font-weight:700;line-height:18px;color:#bbb}
.special-text{left:491px;top:365px;font-size:6px;line-height:10px;color:#bbb;width:100px}
.thumb{top:320px;width:95px;height:65px;background:linear-gradient(160deg,#d8b08a,#8a5a35 55%,#5a3a22)}
.arrow{top:348px;width:0;height:0;border-top:4px solid transparent;border-bottom:4px solid transparent}

/* products */
.stage{left:455px;top:401px;width:513px;height:230px;background:var(--stage)}
.card{left:478px;top:418px;width:471px;height:197px;background:var(--white)}
.photo{top:436px;width:105px;height:121px}
.price{width:46px;height:46px;border-radius:50%;background:var(--red);color:var(--white);text-align:center;border:2px dotted #e45;padding-top:6px}
.price small{display:block;font-size:5.5px}
.price strong{display:block;font-size:15px;line-height:15px}
.prod{top:559px;font-size:9px;line-height:10.5px;color:#444}
.prod b{color:#333}

/* trust */
.pay{left:292px;top:668px;width:153px;height:65px;border:1px solid #ddd;padding:11px 15px}
.pay h4{font-size:10px;font-weight:400;color:#777;padding-bottom:5px;border-bottom:1px solid #e5e5e5}
.cards{display:flex;gap:3px;margin-top:9px}
.cards span{width:19px;height:12px;background:#dcdcdc;border:1px solid #c8c8c8}
.badge{background:#d9d9d9}

/* footer */
.footer{left:0;top:763px;width:1200px;height:189px;background:var(--footer)}
.base{left:0;top:952px;width:1200px;height:48px;background:var(--base);color:#999;font-size:6.5px;text-align:center;padding-top:23px}
.fcol{top:800px;color:#aaa}
.fcol h5{font-size:11px;font-weight:400;color:var(--white);margin-bottom:14px}
.fcol ul{list-style:none;font-size:7px;line-height:10.2px}
.news-text{left:765px;top:826px;font-size:7px;color:#bbb}
.news-field{left:765px;top:842px;width:155px;height:21px;background:#555}
.news-btn{left:920px;top:842px;width:48px;height:21px;background:var(--blue);color:#112;font-size:7px;font-weight:700;display:flex;align-items:center;justify-content:center}
</style>
</head>
<body>
<div class="page">

  <div class="abs brand"><span class="brand-mark"></span><span class="brand-name">Quvanta</span></div>
  <div class="abs tagline">Flooring For Every Room</div>
  <div class="abs util" style="left:682px">Order Tracking | FAQ | My Account</div>
  <div class="abs util" style="left:818px">In Your Cart <b>(0)</b></div>
  <div class="abs proceed">Procede</div>
  <div class="abs proceed-go">
    <svg width="20" height="20" viewBox="0 0 20 20"><path d="M8 5l5 5-5 5" fill="none" stroke="#fff" stroke-width="2.5"/></svg>
  </div>
  <div class="abs nav" style="left:444px">Laminate</div>
  <div class="abs nav" style="left:503px">Hardwood</div>
  <div class="abs nav" style="left:564px">Area Rugs</div>
  <div class="abs nav" style="left:626px">Bamboo</div>
  <div class="abs nav" style="left:668px">Cork</div>
  <div class="abs nav" style="left:707px">Vinyl</div>
  <div class="abs nav" style="left:748px">Carpet Tile</div>
  <div class="abs nav" style="left:810px">Tile</div>
  <div class="abs nav" style="left:850px">Clocks</div>
  <div class="abs nav" style="left:893px">Bath</div>
  <div class="abs nav" style="left:932px">Clearance</div>

  <div class="abs band"></div>

  <div class="abs search"><div class="search-field">Search Products</div></div>
  <div class="abs search-btn">
    <svg width="22" height="18" viewBox="0 0 22 18"><circle cx="10" cy="8" r="4" fill="none" stroke="#fff" stroke-width="1.5"/><path d="M13 11l4 4" stroke="#fff" stroke-width="1.8"/></svg>
  </div>

  <div class="abs side-head" style="top:120px">Shop By Brand</div>
  <ul class="abs side-list" style="top:142px;height:144px">
    <li>Laminate Flooring</li><li>Hardwood Flooring</li><li>Area Rugs</li><li>Bamboo Flooring</li><li>Cork Flooring</li><li>Luxury Vinyl Flooring</li><li>Carpet Tile</li><li>Tile Backsplash</li><li>Tile Backsplash</li><li>Bath Clearance</li>
  </ul>

  <div class="abs side-head" style="top:303px;padding-left:18px">Home Decor</div>
  <ul class="abs side-list" style="top:325px;height:63px;padding-top:11px">
    <li>Laminate Flooring</li><li>Hardwood Flooring</li><li>Area Rugs</li>
  </ul>

  <div class="abs side-head" style="top:394px;padding-left:18px">Home Decor</div>
  <ul class="abs side-list" style="top:416px;height:64px;padding-top:11px">
    <li>Laminate Flooring</li><li>Hardwood Flooring</li><li>Area Rugs</li>
  </ul>

  <div class="abs offer">
    <h3>Offer Price</h3>
    <p>Offering discount prices on <span>laminate</span>, <span>hardwood</span>, <span>cork</span>, <span>bamboo</span>, <span>vinyl</span> and area rugs from the brands you know and trust.</p>
  </div>
  <div class="abs promo-btn">CURRENT PROMOTION</div>

  <div class="abs hero-frame"></div>
  <div class="abs hero-art" role="img" aria-label="Holiday banner with red ornaments and hand-lettered 'Deck the Halls with Savings! free shipping ends monday! click for details'"></div>

  <div class="abs samples"></div>
  <div class="abs samples-title">FREE</div>
  <div class="abs samples-sub">SAMPLES</div>
  <div class="abs samples-notch"></div>
  <div class="abs samples-box">Completely Free.<br>No Credit card required.</div>

  <div class="abs special"></div>
  <div class="abs special-title">SPECIAL<br>OFFER</div>
  <div class="abs special-text">Lorem ipsum dolor sit amet, consectetur adipisicing elit</div>
  <div class="abs arrow" style="left:613px;border-right:6px solid #aaa"></div>
  <div class="abs thumb" style="left:632px" role="img" aria-label="Stacked wood flooring planks sample"></div>
  <div class="abs thumb" style="left:733px" role="img" aria-label="Stacked wood flooring planks sample"></div>
  <div class="abs thumb" style="left:835px" role="img" aria-label="Stacked wood flooring planks sample"></div>
  <div class="abs arrow" style="left:942px;border-left:6px solid #aaa"></div>

  <div class="abs stage"></div>
  <div class="abs card"></div>

  <div class="abs photo" style="left:498px;background:linear-gradient(180deg,#8fc3c9 0%,#a9a49a 40%,#6b5a48 100%)" role="img" aria-label="Seaside room with gray laminate floor"></div>
  <div class="abs price" style="left:560px;top:533px"><small>starting at</small><strong>2.49</strong><small>sq. ft.</small></div>
  <div class="abs prod" style="left:498px"><b>Oakwell</b><br>Coastal Drift<br>12mm Laminate</div>

  <div class="abs photo" style="left:659px;background:linear-gradient(180deg,#4a3a2c 0%,#8a7a68 40%,#6b4628 100%)" role="img" aria-label="Living room with fireplace and acacia hardwood floor"></div>
  <div class="abs price" style="left:721px;top:533px"><small>starting at</small><strong>4.99</strong><small>sq. ft.</small></div>
  <div class="abs prod" style="left:659px"><b>Oakwell</b><br>Timber Hollow<br>Acacia Hardwood</div>

  <div class="abs photo" style="left:824px;background:linear-gradient(180deg,#7a6a55 0%,#b0a590 45%,#5a4a38 100%)" role="img" aria-label="Kitchen with bar stools and tile-look vinyl floor"></div>
  <div class="abs price" style="left:886px;top:533px"><small>starting at</small><strong>3.79</strong><small>sq. ft.</small></div>
  <div class="abs prod" style="left:824px"><b>Veltrane</b><br>Duratile<br>Luxury Vinyl Tile</div>

  <div class="abs pay">
    <h4>Payment Method</h4>
    <div class="cards"><span></span><span></span><span></span><span></span><span></span><span></span></div>
  </div>
  <div class="abs badge" style="left:492px;top:668px;width:92px;height:56px;border-radius:4px"></div>
  <div class="abs badge" style="left:611px;top:682px;width:36px;height:32px;border-radius:50%"></div>
  <div class="abs badge" style="left:683px;top:688px;width:70px;height:20px;border-radius:3px"></div>
  <div class="abs badge" style="left:784px;top:684px;width:32px;height:32px;border-radius:50%"></div>
  <div class="abs badge" style="left:855px;top:690px;width:36px;height:18px"></div>
  <div class="abs badge" style="left:922px;top:686px;width:46px;height:22px"></div>

  <div class="abs footer"></div>
  <div class="abs fcol" style="left:292px">
    <h5>Products</h5>
    <ul><li>Laminate</li><li>Hardwood</li><li>Area Rugs</li><li>Bamboo</li><li>&nbsp;Cork</li><li>Vinyl</li><li>Carpet Tile</li><li>Tile</li><li>Clocks</li><li>&nbsp;Bath</li><li>Clearance</li></ul>
  </div>
  <div class="abs fcol" style="left:462px">
    <h5>Site Info</h5>
    <ul><li>Ordering</li><li>Pricing</li><li>Privacy Policy</li><li>Return Policy</li><li>Shipping</li><li>Sitemap</li></ul>
  </div>
  <div class="abs fcol" style="left:605px">
    <h5>About Us</h5>
    <ul><li>About us</li><li>Careers</li><li>Consumer reviews</li><li>Contact us</li><li>FAQ</li></ul>
  </div>
  <div class="abs fcol" style="left:765px"><h5>Newsletter</h5></div>
  <div class="abs news-text">Lorem ipsum dolor sit amet, consectetur adipisicing elit</div>
  <div class="abs news-field"></div>
  <div class="abs news-btn">Submit</div>

  <div class="abs base">©1999-2013 Northline Home Goods, Inc. All rights reserved. QUVANTA, QUVANTA OUTLET, and QUVANTA.COM are trademarks of Northline Home Goods, Inc. or its affiliates.</div>
</div>
</body>
</html>
```